Business card design for Allied Healthcare provider

We would like a design for front and back of business cards. The design must resonate with all levels of customers from patients, to other health providers and medical. Must also resonate with corporate customers

Target Market(s)

patients, medical practitioners, other health providers and corporate.

Industry/Entity Type

healthcare

Contact Information for Business Card

name, logo, phone and fax numbers, email, website

Requirements
Must have
• not allowing me to change this, but the card must be double sided!! Please take note
Nice to have
• a fresh yet bold design to catch attention.

```html
<!DOCTYPE html>
<html lang="en">
<head>
<meta charset="utf-8">
<title>carevale business card – front and back</title>
<link rel="stylesheet" href="https://fonts.googleapis.com/css2?family=Poppins:wght@700&family=Arimo:wght@400&display=swap">
<style>
  :root {
    --navy: #172a5c;
    --navy-deep: #122250;
    --navy-light: #3a5591;
    --gold: #f2ae1c;
    --white: #ffffff;
    --backdrop: #d9d9db;
  }
  * { box-sizing: border-box; margin: 0; padding: 0; }
  html, body { width: 1200px; height: 801px; overflow: hidden; }
  body {
    background: var(--backdrop);
    font-family: "Arimo", Arial, sans-serif;
    position: relative;
  }
  .card {
    position: absolute;
    top: 240px;
    width: 540px;
    height: 310px;
    border-radius: 26px;
    background: var(--navy);
    border-bottom: 5px solid var(--gold);
    overflow: hidden;
  }
  .card--front { left: 45px; }
  .card--back { left: 615px; }

  .wordmark { position: absolute; display: flex; align-items: center; gap: 8px; }
  .wordmark__dot { width: 12px; height: 12px; border-radius: 50%; background: var(--gold); flex: none; }
  .wordmark__name {
    font-family: "Poppins", Arial, sans-serif;
    font-weight: 700;
    color: var(--white);
    letter-spacing: 0.5px;
    line-height: 1;
  }

  .card--front .wordmark { left: 190px; top: 58px; }
  .card--front .wordmark__name { font-size: 38px; }

  .divider { position: absolute; height: 1.5px; background: var(--white); }
  .divider--main { left: 120px; right: 40px; top: 188px; }
  .divider--short { left: 34px; width: 110px; top: 210px; }

  .holder { position: absolute; left: 34px; top: 140px; }
  .holder__name {
    font-family: "Poppins", Arial, sans-serif;
    font-weight: 700;
    font-size: 24px;
    color: var(--gold);
    line-height: 1.1;
  }
  .holder__role { font-size: 15px; color: var(--white); margin-top: 4px; }

  .address {
    position: absolute; right: 40px; top: 140px;
    text-align: right; color: var(--white); font-size: 14px; line-height: 1.35;
  }

  .contacts { position: absolute; left: 34px; top: 220px; list-style: none; }
  .contacts li {
    display: flex; align-items: center; gap: 10px;
    color: var(--white); font-size: 14.5px; line-height: 19px;
  }
  .contacts svg { width: 13px; height: 13px; flex: none; }

  .emboss-field { position: absolute; inset: 0; }
  .card--back .wordmark { left: 230px; top: 172px; }
  .card--back .wordmark__name { font-size: 34px; }
</style>
</head>
<body>
  <section class="card card--front" aria-label="Card front">
    <div class="wordmark">
      <span class="wordmark__dot"></span>
      <span class="wordmark__name">carevale</span>
    </div>

    <div class="holder">
      <div class="holder__name">Daniel Hart</div>
      <div class="holder__role">Manager</div>
    </div>
    <div class="address">Your address, city<br>state, ZIP 0000</div>

    <div class="divider divider--main"></div>
    <div class="divider divider--short"></div>

    <ul class="contacts">
      <li>
        <svg viewBox="0 0 16 16" aria-hidden="true"><path fill="#f2ae1c" d="M3.5 1.5l2.5 0 1 3.5-1.8 1.2a8 8 0 0 0 4.6 4.6L11 9l3.5 1v2.5c0 1-1 2-2 2A11 11 0 0 1 1.5 3.5c0-1 1-2 2-2z"/></svg>
        <span>123-456-2100</span>
      </li>
      <li>
        <svg viewBox="0 0 16 16" aria-hidden="true"><g fill="none" stroke="#f2ae1c" stroke-width="1.6"><rect x="2" y="6" width="12" height="8" rx="1"/><path d="M4.5 6V1.5h6l1 1V6"/></g><rect x="5" y="9" width="6" height="2" fill="#f2ae1c"/></svg>
        <span>123-456-2100</span>
      </li>
      <li>
        <svg viewBox="0 0 16 16" aria-hidden="true"><g fill="none" stroke="#f2ae1c" stroke-width="1.5"><rect x="1.5" y="3.5" width="13" height="9" rx="1"/><path d="M1.5 4l6.5 5 6.5-5"/></g></svg>
        <span>youremail@mailbox.com</span>
      </li>
      <li>
        <svg viewBox="0 0 16 16" aria-hidden="true"><g fill="none" stroke="#f2ae1c" stroke-width="1.4"><circle cx="8" cy="8" r="6.3"/><ellipse cx="8" cy="8" rx="2.8" ry="6.3"/><path d="M1.7 8h12.6M2.8 5h10.4M2.8 11h10.4"/></g></svg>
        <span>www.yourwebsite.com</span>
      </li>
    </ul>
  </section>

  <section class="card card--back" aria-label="Card back">
    <svg class="emboss-field" role="img" aria-label="Embossed repeating brand-mark pattern across the card back" viewBox="0 0 540 310" preserveAspectRatio="none">
      <defs>
        <linearGradient id="emboss-tone" x1="0" y1="0" x2="1" y2="1">
          <stop offset="0" stop-color="#122250"/>
          <stop offset="0.6" stop-color="#1a2e62"/>
          <stop offset="1" stop-color="#3a5591"/>
        </linearGradient>
      </defs>
      <rect width="540" height="310" fill="url(#emboss-tone)"/>
    </svg>
    <div class="wordmark">
      <span class="wordmark__dot"></span>
      <span class="wordmark__name">carevale</span>
    </div>
  </section>
</body>
</html>
```